Veteran Owned General Contractor needs Bold New Business Cards

We are a service disabled veteran owned small business. We're a general contractor that specializes in excavation, underground utilities, site work, land clearing and demolition. We would like a fresh, simple, bold, new look for our business cards. We're open to ideas! We'd like to incorporate the following information on the card:

Company Name & Logo, Name of Person, Job Title, Office Phone, Fax, Cell Phone, Email Address, Website, SDVOSB

Our logo is included. We look forward to your thoughts.

Thank you!
Updates

Reason: Hello Due to the overwhelming response to this project, we are extending the deadline one time to allow for improved communication and feedback with the top candidates. We would like to thank everyone for their hard work and exceptional creativity! Thank you

Industry/Entity Type

Business

Contact Information for Business Card

Font styles to use
Sans Serif

Requirements
Nice to have
• As we are a veteran owned company, it would be nice to incorporate an American flag into the design. Maybe on the back?

```html
<!DOCTYPE html>
<html lang="en">
<head>
<meta charset="utf-8">
<title>Groundline Inc – Business Card</title>
<link rel="stylesheet" href="https://fonts.googleapis.com/css2?family=Open+Sans:wght@400;600;800&display=swap">
<style>
  :root {
    --backdrop: #9b9b9b;
    --card: #f4f4f2;
    --green: #5aad35;
    --ink-dark: #2e2e2e;
    --ink-grey: #5a5a5a;
    --white: #ffffff;
    --tint-blue: #d3dbe9;
    --tint-red: #ecd6dc;
    --tint-light: #f2eff0;
  }
  * { margin: 0; padding: 0; box-sizing: border-box; }
  html, body {
    width: 1105px;
    height: 1200px;
    overflow: hidden;
  }
  body {
    background: var(--backdrop);
    font-family: "Open Sans", Arial, sans-serif;
    position: relative;
  }
  .card {
    position: absolute;
    left: 182px;
    width: 748px;
    height: 427px;
    background: var(--card);
    overflow: hidden;
  }
  .card--front { top: 119px; }
  .card--back  { top: 635px; }

  .card__wave {
    position: absolute;
    inset: 0;
    width: 100%;
    height: 100%;
  }

  /* Brand block */
  .brand {
    position: absolute;
    display: flex;
    flex-direction: column;
    align-items: center;
  }
  .brand__mark {
    width: 64px;
    height: 64px;
    background: var(--ink-dark);
    border-radius: 10px;
  }
  .brand__name {
    color: var(--green);
    font-weight: 800;
    font-size: 36px;
    letter-spacing: 1px;
    line-height: 1;
    white-space: nowrap;
  }
  .card--front .brand { left: 50px; top: 50px; width: 300px; }
  .card--front .brand__name { margin-top: 46px; font-size: 34px; }
  .card--back .brand { left: 0; right: 0; top: 141px; }
  .card--back .brand__name { margin-top: 38px; }

  /* Contact block */
  .contact {
    position: absolute;
    right: 32px;
    top: 184px;
    text-align: right;
    color: var(--white);
  }
  .contact__name {
    font-size: 23px;
    font-weight: 600;
    line-height: 1.2;
  }
  .contact__title {
    font-size: 19px;
    font-weight: 400;
    line-height: 1.3;
    margin-bottom: 22px;
  }
  .contact__list { list-style: none; }
  .contact__item {
    display: flex;
    justify-content: flex-end;
    align-items: center;
    gap: 9px;
    font-size: 18px;
    height: 29px;
  }
  .contact__icon { width: 18px; height: 18px; flex: none; }

  /* Back */
  .flag-field {
    position: absolute;
    inset: 0;
    background:
      radial-gradient(ellipse at 20% 25%, var(--tint-blue) 0%, transparent 55%),
      linear-gradient(160deg, var(--tint-light) 0%, var(--tint-red) 60%, var(--tint-light) 100%);
  }
  .website {
    position: absolute;
    left: 0; right: 0;
    top: 350px;
    text-align: center;
    font-size: 18px;
    letter-spacing: 5px;
    color: var(--ink-grey);
  }
</style>
</head>
<body>

<section class="card card--front" aria-label="Business card front">
  <svg class="card__wave" viewBox="0 0 748 427" preserveAspectRatio="none" aria-hidden="true">
    <path fill="var(--green)" d="M0 338 C 90 395, 180 420, 250 402 C 340 372, 420 170, 748 88 L748 427 L0 427 Z"/>
    <path fill="none" stroke="var(--green)" stroke-width="2.5" d="M0 322 C 90 382, 180 402, 250 386 C 340 356, 420 156, 748 72"/>
  </svg>

  <div class="brand">
    <div class="brand__mark"></div>
    <div class="brand__name">GROUNDLINE INC</div>
  </div>

  <div class="contact">
    <div class="contact__name">Mark Halden</div>
    <div class="contact__title">President</div>
    <ul class="contact__list">
      <li class="contact__item">555 2710 4418
        <svg class="contact__icon" viewBox="0 0 18 18" aria-hidden="true"><path fill="var(--white)" d="M2 6 C2 3 16 3 16 6 L13 8 L12 6 L6 6 L5 8 Z M4 10 L14 10 L15 16 L3 16 Z"/></svg>
      </li>
      <li class="contact__item">555 3986 2207
        <svg class="contact__icon" viewBox="0 0 18 18" aria-hidden="true"><rect x="5" y="1" width="9" height="16" rx="1.5" fill="none" stroke="var(--white)" stroke-width="1.8"/><circle cx="9.5" cy="14" r="1" fill="var(--white)"/></svg>
      </li>
      <li class="contact__item">555 6149 7730
        <svg class="contact__icon" viewBox="0 0 18 18" aria-hidden="true"><rect x="4" y="1" width="10" height="6" fill="var(--white)"/><rect x="1" y="8" width="16" height="8" rx="1" fill="var(--white)"/><rect x="4" y="11" width="10" height="2" fill="var(--green)"/></svg>
      </li>
      <li class="contact__item">mark@groundline.com
        <svg class="contact__icon" viewBox="0 0 18 18" aria-hidden="true"><rect x="1" y="4" width="16" height="10" fill="var(--white)"/><path d="M1 4 L9 10 L17 4" fill="none" stroke="var(--green)" stroke-width="1.4"/></svg>
      </li>
      <li class="contact__item">www.groundline.com
        <svg class="contact__icon" viewBox="0 0 18 18" aria-hidden="true"><circle cx="9" cy="9" r="8" fill="var(--white)"/><path d="M5 6 L9 5 L10 9 L7 12 Z M11 11 L14 10 L13 14 Z" fill="var(--green)"/></svg>
      </li>
    </ul>
  </div>
</section>

<section class="card card--back" aria-label="Business card back">
  <div class="flag-field" role="img" aria-label="Faded, weathered American flag filling the card background"></div>
  <div class="brand">
    <div class="brand__mark"></div>
    <div class="brand__name">GROUNDLINE INC</div>
  </div>
  <div class="website">www.groundline.com</div>
</section>

</body>
</html>
```